PVQ BOOK COVER 6 X 9 - MARKET LEADING LEADERSHIP BOOK

I need a book cover designed for a book called Steering Through the Era of Circuits – Enduring Insight for an Automated Century and some more stuff, which you can see in the image I generated. I created a basic cover, but it needs to wow; it's about leadership, ancient wisdom, and AI. This book offers a unique approach: combining 2,000-year-old Stoic philosophy with practical frameworks for modern AI-age leadership challenges. Rather than another technical book about AI, this is a deeply human guide for leaders who want to harness AI's power while preserving their organisation's humanity.

Target Market(s)

EXECUTIVES, LEADERS MANAGERS DEALING WITH AI

Industry/Entity Type

LEADERSHIP

Requirements
Must have
• MUSIC BE CLASSY AND A SOLID COMBINATION OF ANCIENT WISDOM AND FUTURISTIC AI
Nice to have
• GIVE ME THE BEST YOU HAVE
Should not have
• NON

```html
<!DOCTYPE html>
<html lang="en">
<head>
<meta charset="utf-8">
<title>Steering Through the Era of Circuits – Book Cover</title>
<link href="https://fonts.googleapis.com/css2?family=Bebas+Neue&family=Montserrat:wght@500;600;700&display=swap" rel="stylesheet">
<style>
  :root {
    --page: #ffffff;
    --cover: #0e0e0e;
    --ink: #ffffff;
    --cyan: #16cfe9;
    --blue: #2563f5;
    --stone-light: #b99a68;
    --stone-mid: #8a6433;
    --stone-dark: #3a2814;
  }
  * { margin: 0; padding: 0; box-sizing: border-box; }
  html, body {
    width: 863px;
    height: 1200px;
    overflow: hidden;
    background: var(--page);
  }
  .canvas {
    position: relative;
    width: 863px;
    height: 1200px;
    background: var(--page);
  }
  .cover {
    position: absolute;
    left: 54px;
    top: 66px;
    width: 754px;
    height: 1067px;
    background: var(--cover);
    overflow: hidden;
  }
  .title-art {
    position: absolute;
    left: 0;
    top: 0;
    width: 754px;
    height: 500px;
  }
  .title-main {
    font-family: "Bebas Neue", "Oswald", sans-serif;
    fill: var(--ink);
  }
  .title-line {
    font-family: "Montserrat", sans-serif;
    font-weight: 500;
    fill: var(--ink);
  }
  .title-accent {
    font-family: "Montserrat", sans-serif;
    font-weight: 600;
  }
  .subtitle {
    position: absolute;
    left: 56px;
    top: 426px;
    font-family: "Montserrat", sans-serif;
    font-weight: 600;
    font-size: 22px;
    line-height: 32px;
    letter-spacing: 2.5px;
    color: var(--ink);
    text-transform: uppercase;
  }
  .subtitle .accent { color: var(--cyan); }
  .hero-art {
    position: absolute;
    left: 156px;
    top: 532px;
    width: 430px;
    height: 412px;
    border-radius: 6px;
    background:
      radial-gradient(ellipse at 38% 40%, var(--stone-light) 0%, var(--stone-mid) 45%, var(--stone-dark) 80%, var(--cover) 100%);
  }
  .author {
    position: absolute;
    left: 0;
    width: 754px;
    top: 978px;
    text-align: center;
    font-family: "Bebas Neue", "Oswald", sans-serif;
    font-size: 44px;
    line-height: 1;
    letter-spacing: 0.42em;
    padding-left: 0.42em;
    color: var(--ink);
  }
</style>
</head>
<body>
<div class="canvas">
  <section class="cover">
    <svg class="title-art" viewBox="0 0 754 500" xmlns="http://www.w3.org/2000/svg">
      <defs>
        <linearGradient id="accentGradient" x1="0" y1="0" x2="0" y2="1">
          <stop offset="0" stop-color="var(--blue)"/>
          <stop offset="0.5" stop-color="var(--cyan)"/>
          <stop offset="1" stop-color="var(--blue)"/>
        </linearGradient>
      </defs>
      <text class="title-main" x="56" y="217" font-size="240" textLength="642" lengthAdjust="spacingAndGlyphs">STEERING</text>
      <text class="title-line" x="56" y="294" font-size="66" textLength="642" lengthAdjust="spacingAndGlyphs">THROUGH THE ERA OF</text>
      <text class="title-accent" x="56" y="405" font-size="130" fill="url(#accentGradient)" textLength="642" lengthAdjust="spacingAndGlyphs">CIRCUITS</text>
    </svg>

    <p class="subtitle">
      <span class="accent">Enduring Insight</span><br>
      For an <span class="accent">Automated</span> Century
    </p>

    <div class="hero-art" role="img" aria-label="Classical marble bust of a bearded philosopher dissolving into pixels beside a weathered stone tablet carved with a glowing blue circuit chip"></div>

    <p class="author">Author Name</p>
  </section>
</div>
</body>
</html>
```